Building company buisness cards

We are looking for a sharp modern new look for our business cards.
We are a New Zealand based company that specialises in house and land packages.
We have attached a photo of the current logo and would like to see if it can be improved somehow if needed.
We are open to any colours but we have chosen green at this stage.
Feel free to change the font and make the logo smarter looking.
Play with the colours and see what looks best.

We want a card that looks so good know one will want to throw it away!

Target Market(s)

Home buyers

Industry/Entity Type

Building

Contact Information for Business Card

Dorian Keswick
0217392604
dkeswick@tidewellhomecraft.co.nz
tidewellhomecraft.co.nz

Font styles to use
Serif
Sans Serif

Colors

Designer to choose colors to be used in the design.

Requirements
Must have
• Logo and company name on one side, details on the other side
Nice to have
• Color codes for the original green are HEX #4a8028, RGB(74,128,40), CMYK(42,0,69,50)
• Round corners, Raised and/or spot UV

```html
<!DOCTYPE html>
<html lang="en">
<head>
<meta charset="utf-8">
<title>Tidewell Homecraft – Business Cards</title>
<link rel="stylesheet" href="https://fonts.googleapis.com/css2?family=Quicksand:wght@500;700&display=swap">
<style>
  :root {
    --backdrop: #232a36;
    --card: #141516;
    --card-edge: #0c0c0d;
    --pattern-a: #1b1c1e;
    --pattern-b: #121314;
    --brand-green: #4a8028;
    --text-light: #e6e8e4;
  }
  * { box-sizing: border-box; margin: 0; padding: 0; }
  html, body {
    width: 1200px;
    height: 800px;
    overflow: hidden;
    background: var(--backdrop);
    font-family: "Quicksand", sans-serif;
  }
  .canvas {
    position: relative;
    width: 1200px;
    height: 800px;
  }
  .card {
    position: absolute;
    left: 320px;
    width: 560px;
    height: 320px;
    background: var(--card);
    border-radius: 14px;
    box-shadow: 0 2px 0 var(--card-edge), 0 18px 40px rgba(0,0,0,0.35);
    overflow: hidden;
  }
  .card--front { top: 50px; }
  .card--back { top: 430px; }

  .front-texture {
    position: absolute;
    inset: 0;
    background: radial-gradient(circle at 50% 45%, var(--pattern-a), var(--pattern-b));
  }
  .front-brand {
    position: absolute;
    left: 0; right: 0;
    top: 50%;
    transform: translateY(-50%);
    display: flex;
    align-items: center;
    justify-content: center;
    gap: 12px;
  }
  .brand-mark {
    width: 14px;
    height: 14px;
    background: var(--brand-green);
  }
  .brand-name {
    color: var(--brand-green);
    font-weight: 700;
    font-size: 34px;
    letter-spacing: 0.2px;
    line-height: 1;
  }

  .back-brand {
    position: absolute;
    right: 40px;
    top: 40px;
    display: flex;
    align-items: center;
    gap: 10px;
  }
  .back-brand .brand-name { font-size: 26px; }
  .back-brand .brand-mark { width: 11px; height: 11px; }

  .holder-name {
    position: absolute;
    left: 40px;
    top: 140px;
    color: var(--brand-green);
    font-weight: 700;
    font-size: 26px;
  }
  .contact-list {
    position: absolute;
    left: 40px;
    bottom: 34px;
    list-style: none;
  }
  .contact-item {
    display: flex;
    align-items: center;
    gap: 10px;
    color: var(--text-light);
    font-weight: 500;
    font-size: 14px;
    line-height: 24px;
  }
  .contact-icon { width: 14px; height: 14px; flex: none; }
</style>
</head>
<body>
<main class="canvas">

  <section class="card card--front" aria-label="Card front">
    <div class="front-texture" role="img" aria-label="Raised tone-on-tone repeating pattern of the company mark"></div>
    <div class="front-brand">
      <span class="brand-mark"></span>
      <span class="brand-name">tidewell homecraft</span>
    </div>
  </section>

  <section class="card card--back" aria-label="Card back">
    <div class="back-brand">
      <span class="brand-mark"></span>
      <span class="brand-name">tidewell homecraft</span>
    </div>

    <h1 class="holder-name">Dorian Keswick</h1>

    <ul class="contact-list">
      <li class="contact-item">
        <svg class="contact-icon" viewBox="0 0 16 16" aria-hidden="true">
          <rect x="0" y="0" width="16" height="16" rx="3" fill="var(--brand-green)"/>
          <path d="M5 3.5l1.6 2.2-1 1.1c.6 1.3 1.6 2.3 2.9 2.9l1.1-1 2.2 1.6-.7 1.7C7.6 12 4 8.4 3.5 4.2z" fill="var(--card)"/>
        </svg>
        <span>0217392604</span>
      </li>
      <li class="contact-item">
        <svg class="contact-icon" viewBox="0 0 16 16" aria-hidden="true">
          <rect x="0" y="0" width="16" height="16" rx="3" fill="var(--brand-green)"/>
          <rect x="3" y="4.5" width="10" height="7" fill="none" stroke="var(--card)" stroke-width="1.2"/>
          <path d="M3 4.5l5 4 5-4" fill="none" stroke="var(--card)" stroke-width="1.2"/>
        </svg>
        <span>dkeswick@tidewellhomecraft.co.nz</span>
      </li>
      <li class="contact-item">
        <svg class="contact-icon" viewBox="0 0 16 16" aria-hidden="true">
          <circle cx="8" cy="8" r="7" fill="none" stroke="var(--brand-green)" stroke-width="1.4"/>
          <ellipse cx="8" cy="8" rx="3" ry="7" fill="none" stroke="var(--brand-green)" stroke-width="1.1"/>
          <line x1="1" y1="8" x2="15" y2="8" stroke="var(--brand-green)" stroke-width="1.1"/>
        </svg>
        <span>tidewellhomecraft.co.nz</span>
      </li>
    </ul>
  </section>

</main>
</body>
</html>
```